" ELA NAO FOI ABERTA AINDA MAS SERA EM 20 DIAS. A VARTEMI - uma empresa especializada na prestação de serviços terceirizados integrados, auxiliando nossos clientes a reduzir custos indiretos, focar em seu negócio principal, sem se preocupar com serviços de apoio, como limpeza, copa, portaria, segurança, administrativo, zeladoria, telefonia e recepção. Uma empresa ou Condomínio apresenta necessidades diversas para se manter operando de maneira lucrativa e segura. Antes, cada negócio precisava atender às demandas por meio de sua infraestrutura interna. Mas uma opção vantajosa vem crescendo no mercado e merece destaque atualmente: a terceirização de atividades "

```html
<!DOCTYPE html>
<html lang="pt-BR">
<head>
<meta charset="UTF-8">
<title>VARTEMI — Pasta institucional</title>
<link rel="stylesheet" href="https://fonts.googleapis.com/css2?family=Montserrat:wght@400;700&display=swap">
<style>
  :root {
    --backdrop: #2b2b2d;
    --paper: #ffffff;
    --paper-shade: #ececee;
    --cover: #111113;
    --cover-light: #2a2a2e;
    --brand-gold: #c9c45a;
    --brand-blue: #2f4f9e;
    --ink: #555a60;
    --ink-light: #8a8f96;
  }
  * { margin: 0; padding: 0; box-sizing: border-box; }
  html, body {
    width: 1200px; height: 1200px; overflow: hidden;
    background: var(--backdrop);
    font-family: "Montserrat", sans-serif;
  }
  .folder-spread {
    position: absolute;
    left: 110px; top: 200px;
    width: 980px; height: 700px;
    display: flex;
    box-shadow: 0 20px 60px rgba(0,0,0,0.5);
  }
  .folder-page {
    position: relative;
    width: 490px; height: 700px;
    overflow: hidden;
  }
  .folder-inside { background: var(--paper); }
  .folder-cover { background: var(--cover); }

  .inside-decoration {
    position: absolute;
    left: 120px; top: 90px;
    width: 420px; height: 520px;
    border-radius: 60% 0 0 40%;
    background: radial-gradient(ellipse at 70% 40%, var(--paper-shade), rgba(255,255,255,0) 70%);
  }
  .cover-decoration {
    position: absolute;
    left: -40px; top: 0;
    width: 560px; height: 620px;
    background: radial-gradient(ellipse at 55% 40%, var(--cover-light), rgba(17,17,19,0) 65%);
  }

  .brand-mark {
    position: absolute;
    display: flex; align-items: center; gap: 8px;
    font-weight: 700; color: var(--brand-gold);
    letter-spacing: 0.12em;
  }
  .brand-mark .brand-dot {
    border-radius: 50%;
    background: var(--brand-blue);
  }
  .inside-brand { left: 50%; top: 70px; transform: translateX(-50%); font-size: 18px; }
  .inside-brand .brand-dot { width: 14px; height: 14px; }
  .cover-brand { left: 50%; top: 270px; transform: translateX(-50%); font-size: 40px; }
  .cover-brand .brand-dot { width: 28px; height: 28px; }

  .contact-row {
    position: absolute;
    left: 30px; right: 30px; bottom: 40px;
    display: flex; justify-content: space-between; align-items: flex-start;
    font-size: 8px; line-height: 1.45; color: var(--ink);
  }
  .contact-item { display: flex; gap: 6px; align-items: flex-start; }
  .contact-item svg { flex: none; width: 12px; height: 12px; }

  .pocket-slit { position: absolute; left: 0; bottom: 0; }
</style>
</head>
<body>
  <main class="folder-spread">
    <section class="folder-page folder-inside">
      <div class="inside-decoration" role="img" aria-label="Grande marca da empresa em cinza claro como marca d'água"></div>
      <div class="brand-mark inside-brand"><span class="brand-dot"></span>VARTEMI</div>
      <footer class="contact-row">
        <div class="contact-item">
          <svg viewBox="0 0 12 12"><circle cx="6" cy="6" r="5.5" fill="var(--ink)"/><path d="M6 3a2 2 0 0 1 2 2c0 1.5-2 3.5-2 3.5S4 6.5 4 5a2 2 0 0 1 2-2z" fill="#fff"/></svg>
          <span>Rua das Acácias, 120<br>Centro, Niterói - RJ<br>CEP 24000-000</span>
        </div>
        <div class="contact-item">
          <svg viewBox="0 0 12 12"><circle cx="6" cy="6" r="5.5" fill="var(--ink)"/><rect x="3" y="4" width="6" height="4" fill="none" stroke="#fff" stroke-width="0.8"/><path d="M3 4l3 2.3L9 4" fill="none" stroke="#fff" stroke-width="0.8"/></svg>
          <span>contato@vartemi.com.br</span>
        </div>
        <div class="contact-item">
          <svg viewBox="0 0 12 12"><circle cx="6" cy="6" r="5.5" fill="var(--ink)"/><path d="M4.2 3.5l1 1-.6.8c.4.8 1 1.4 1.8 1.8l.8-.6 1 1-.7.9C5.6 8.3 3.7 6.4 3.6 4.2z" fill="#fff"/></svg>
          <span>(21) 4000-1234</span>
        </div>
      </footer>
    </section>
    <section class="folder-page folder-cover">
      <div class="cover-decoration" role="img" aria-label="Grande símbolo da marca em cinza escuro como decoração de fundo"></div>
      <div class="brand-mark cover-brand"><span class="brand-dot"></span>VARTEMI</div>
      <svg class="pocket-slit" width="490" height="80" viewBox="0 0 490 80">
        <path d="M0 62 Q20 50 60 50 L380 50 Q430 50 490 32" fill="none" stroke="#4a4a50" stroke-width="2"/>
      </svg>
    </section>
  </main>
</body>
</html>
```